Restaurant menu design

Design fine dinning menu for Indian restaurant. Restaurant location is on river side. So if design has some touch of Yarra river of Melbourne and Indian touch. It is not compulsory. Creative and modern design is required.
I want to print in A3 and folded take away sizes so design should for both.
1. In A3, backside we need to design drink menu. I am attaching our current restaurant menu for drinks name and price.

Target Market(s)

Indian / Australian Customer

Industry/Entity Type

Indian Food, Indian fine dining

Colors
F0912C
F2A743
F7CA91
FBE8D2
FDF5EE

Requirements
Must have
• Simple but district design
Should not have
• common other restaurant type menu. Too many colours.

```html
<!DOCTYPE html>
<html lang="en">
<head>
<meta charset="utf-8">
<title>Tamara's Table – Drinks Menu Spread</title>
<link href="https://fonts.googleapis.com/css2?family=Oswald:wght@400;500;700&family=Roboto+Condensed:wght@400;700&display=swap" rel="stylesheet">
<style>
  :root {
    --backdrop: #d9d9d9;
    --paper: #f4e7d0;
    --paper-edge: #e8d3b0;
    --ink: #4a2e1f;
    --ink-soft: #6e5240;
    --rust: #a2471f;
    --rust-dark: #7e3416;
    --sand: #f7ca91;
    --cream: #fdf5ee;
  }
  * { box-sizing: border-box; margin: 0; padding: 0; }
  html, body { width: 867px; height: 1200px; overflow: hidden; }
  body {
    background: var(--backdrop);
    font-family: "Roboto Condensed", "Arial Narrow", sans-serif;
    color: var(--ink);
    position: relative;
  }
  .spread {
    position: absolute;
    left: 20px; top: 307px;
    width: 827px; height: 585px;
    display: flex;
    background: radial-gradient(ellipse at center, var(--paper) 55%, var(--paper-edge) 100%);
    box-shadow: 0 2px 6px rgba(0,0,0,.25);
  }
  .panel {
    position: relative;
    width: 50%;
    height: 100%;
    padding: 22px 20px;
  }
  .panel::before {
    content: "";
    position: absolute; inset: 10px;
    border: 1.5px solid var(--rust);
    outline: 1px solid var(--rust);
    outline-offset: -4px;
    pointer-events: none;
  }
  .panel--back { display: flex; gap: 16px; border-right: 1px solid rgba(74,46,31,.15); }
  .column { flex: 1; position: relative; z-index: 1; }

  .section-title {
    background: var(--rust);
    color: var(--cream);
    font-family: "Oswald", sans-serif;
    font-weight: 500;
    font-size: 11px;
    letter-spacing: 1px;
    text-align: center;
    padding: 3px 0 2px;
    line-height: 1.1;
    margin: 8px 0 6px;
  }
  .section-title small { display: block; font-size: 7px; letter-spacing: .8px; font-weight: 400; }
  .section-note { font-size: 7px; text-align: center; color: var(--ink-soft); margin: -3px 0 5px; }

  .menu-list { list-style: none; }
  .menu-item { display: flex; justify-content: space-between; font-size: 8.5px; font-weight: 700; line-height: 1.3; }
  .menu-item .price { color: var(--rust); }
  .menu-entry { margin-bottom: 5px; }
  .menu-entry .desc { font-size: 7px; color: var(--ink-soft); line-height: 1.2; }
  .menu-list--compact .menu-item { margin-bottom: 3px; }

  .contact-box {
    margin-top: 14px;
    border: 1px solid var(--rust);
    padding: 7px 8px;
    font-size: 7.5px;
    line-height: 1.45;
    text-align: center;
  }
  .contact-box strong { color: var(--rust); font-family: "Oswald", sans-serif; font-weight: 500; font-size: 8.5px; letter-spacing: .5px; }

  .panel--cover { display: flex; flex-direction: column; align-items: center; padding-top: 32px; }
  .brand-name {
    font-family: "Oswald", sans-serif;
    font-weight: 700;
    font-size: 26px;
    color: var(--ink);
    letter-spacing: .5px;
    border-bottom: 2px solid var(--ink);
    padding: 0 8px 2px;
  }
  .cover-title {
    font-family: "Oswald", sans-serif;
    font-weight: 700;
    font-size: 46px;
    line-height: 1;
    text-align: center;
    margin-top: 26px;
    color: var(--ink);
  }
  .cover-title .accent { display: block; color: var(--rust); }
  .cover-tagline {
    font-family: "Oswald", sans-serif;
    font-size: 10px;
    letter-spacing: 2px;
    margin-top: 8px;
    color: var(--ink-soft);
  }
  .cover-scene {
    width: 340px; height: 210px;
    margin-top: 26px;
    background: linear-gradient(180deg, rgba(244,231,208,0) 0%, #d8c3a2 55%, #bfa27c 100%);
    border-radius: 4px;
  }
  .cover-url {
    margin-top: auto;
    margin-bottom: 8px;
    font-family: "Oswald", sans-serif;
    font-size: 10px;
    letter-spacing: 1.5px;
    color: var(--ink);
  }
</style>
</head>
<body>
  <main class="spread">
    <section class="panel panel--back">
      <div class="column">
        <h2 class="section-title">MOCKTAILS<small>(NON – ALCOHOLIC)</small></h2>
        <ul class="menu-list">
          <li class="menu-entry"><div class="menu-item"><span>Mango Mint Cooler</span><span class="price">$9</span></div><p class="desc">Mango pulp, fresh mint and soda</p></li>
          <li class="menu-entry"><div class="menu-item"><span>Rose Lemonade</span><span class="price">$8</span></div><p class="desc">Rose syrup, lime juice and soda</p></li>
          <li class="menu-entry"><div class="menu-item"><span>Tamarind Spritz</span><span class="price">$9</span></div><p class="desc">Tamarind, ginger ale and chaat masala</p></li>
          <li class="menu-entry"><div class="menu-item"><span>Kesar Sunrise</span><span class="price">$9</span></div><p class="desc">Saffron, orange juice and grenadine</p></li>
          <li class="menu-entry"><div class="menu-item"><span>Lychee Breeze</span><span class="price">$8</span></div><p class="desc">Lychee, lemongrass and crushed ice</p></li>
        </ul>
        <h2 class="section-title">MOCKTAILS<small>(NON – ALCOHOLIC)</small></h2>
        <ul class="menu-list">
          <li class="menu-entry"><div class="menu-item"><span>Virgin Mojito</span><span class="price">$8</span></div><p class="desc">Lime, mint, sugar and soda</p></li>
          <li class="menu-entry"><div class="menu-item"><span>Jaljeera Tonic</span><span class="price">$8</span></div><p class="desc">Cumin, lemon and black salt</p></li>
          <li class="menu-entry"><div class="menu-item"><span>Guava Chilli Punch</span><span class="price">$9</span></div><p class="desc">Pink guava with a chilli rim</p></li>
        </ul>
        <h2 class="section-title">BEER</h2>
        <p class="section-note">330ml each bottle</p>
        <ul class="menu-list menu-list--compact">
          <li class="menu-item"><span>Tiger Lane Lager</span><span class="price">$10</span></li>
          <li class="menu-item"><span>Yarra Pale Ale</span><span class="price">$11</span></li>
          <li class="menu-item"><span>Monsoon Wheat</span><span class="price">$11</span></li>
        </ul>
      </div>

      <div class="column">
        <h2 class="section-title">BEVERAGES<small>(NON – ALCOHOLIC)</small></h2>
        <ul class="menu-list menu-list--compact">
          <li class="menu-item"><span>Masala Chai</span><span class="price">$5</span></li>
          <li class="menu-item"><span>Filter Coffee</span><span class="price">$5</span></li>
          <li class="menu-item"><span>Sweet Lassi</span><span class="price">$7</span></li>
          <li class="menu-item"><span>Salted Lassi</span><span class="price">$7</span></li>
          <li class="menu-item"><span>Fresh Lime Soda</span><span class="price">$6</span></li>
          <li class="menu-item"><span>Soft Drinks</span><span class="price">$4</span></li>
        </ul>
        <h2 class="section-title">SCOTCH<small>WHISKY &amp; BOURBON</small></h2>
        <ul class="menu-list menu-list--compact">
          <li class="menu-item"><span>Highland Single Malt</span><span class="price">$14</span></li>
          <li class="menu-item"><span>Speyside 12 Year</span><span class="price">$15</span></li>
          <li class="menu-item"><span>Islay Peated Malt</span><span class="price">$16</span></li>
          <li class="menu-item"><span>Blended Scotch</span><span class="price">$11</span></li>
          <li class="menu-item"><span>Kentucky Bourbon</span><span class="price">$12</span></li>
          <li class="menu-item"><span>Tennessee Whiskey</span><span class="price">$12</span></li>
        </ul>
        <h2 class="section-title">SPIRITS</h2>
        <ul class="menu-list menu-list--compact">
          <li class="menu-item"><span>London Dry Gin</span><span class="price">$11</span></li>
          <li class="menu-item"><span>Premium Vodka</span><span class="price">$11</span></li>
          <li class="menu-item"><span>Dark Rum</span><span class="price">$10</span></li>
          <li class="menu-item"><span>White Rum</span><span class="price">$10</span></li>
          <li class="menu-item"><span>Silver Tequila</span><span class="price">$12</span></li>
        </ul>
        <div class="contact-box">
          <p>Reservations: 03 5550 1842</p>
          <p>Takeaway: 03 5550 1843</p>
          <p><strong>OPENING HOURS</strong></p>
          <p>Tue – Sun 5pm – 10pm</p>
          <p>12 Riverbank Promenade, Southbank VIC</p>
        </div>
      </div>
    </section>

    <section class="panel panel--cover">
      <h1 class="brand-name">Tamara's Table</h1>
      <p class="cover-title">TASTE<span class="accent">OF INDIA</span></p>
      <p class="cover-tagline">EXPLORE THE FLAVORS OF PARADISE!</p>
      <div class="cover-scene" role="img" aria-label="Sketched riverside restaurant terrace with umbrellas, tables and a bridge in sepia ink"></div>
      <p class="cover-url">WWW.TAMARASTABLE.COM.AU</p>
    </section>
  </main>
</body>
</html>
```